Gearloft forum banner

Need a banner ad for a forum relating to the motor car industry.
I have attached a sample banner , we need ours to be edited to suit our web site - gearloft-example.com.au
Image needs to be roughly 400px by 100px.
We would like to display information like the pic below named kelbanner but with a better design / colour / image combination.

```html
<!DOCTYPE html>
<html lang="en">
<head>
<meta charset="utf-8">
<title>Gearloft forum banner</title>
<link rel="stylesheet" href="https://fonts.googleapis.com/css2?family=Roboto+Condensed:wght@400;700&display=swap">
<style>
  :root {
    --ink: #050505;
    --panel-edge: #3a3a3a;
    --photo-dark: #0b0b0c;
    --photo-mid: #2a2c30;
    --photo-light: #5d6168;
    --text-white: #ffffff;
    --text-soft: #c9c9c9;
  }
  html, body {
    margin: 0;
    padding: 0;
    width: 1200px;
    height: 300px;
    overflow: hidden;
    background: var(--ink);
  }
  .banner {
    position: relative;
    width: 1200px;
    height: 300px;
    overflow: hidden;
    box-sizing: border-box;
    border: 3px solid var(--panel-edge);
    font-family: "Roboto Condensed", "Arial Narrow", sans-serif;
    color: var(--text-white);
  }
  .showroom-photo {
    position: absolute;
    inset: 0;
    background:
      radial-gradient(ellipse 420px 200px at 720px 210px, var(--photo-light) 0%, var(--photo-mid) 45%, transparent 80%),
      radial-gradient(ellipse 300px 120px at 620px 40px, #3b3d42 0%, transparent 75%),
      linear-gradient(90deg, var(--photo-dark) 0%, var(--photo-dark) 30%, #1b1c1f 55%, var(--photo-dark) 100%);
  }
  .site-url {
    position: absolute;
    left: 555px;
    top: 24px;
    font-size: 20px;
    letter-spacing: 1px;
    text-transform: uppercase;
    color: var(--text-soft);
  }
  .brand {
    position: absolute;
    left: 24px;
    top: 82px;
  }
  .brand-name {
    margin: 0;
    font-size: 96px;
    font-weight: 700;
    line-height: 1;
    text-transform: uppercase;
    color: var(--text-white);
  }
  .brand-tagline {
    margin: 8px 0 0 4px;
    font-size: 18px;
    font-weight: 700;
    letter-spacing: 0.5px;
    text-transform: uppercase;
    color: var(--text-white);
  }
  .headline {
    position: absolute;
    right: 30px;
    top: 92px;
    margin: 0;
    font-size: 54px;
    font-weight: 400;
    line-height: 1.08;
    text-align: right;
    color: var(--text-white);
  }
</style>
</head>
<body>
  <div class="banner">
    <div class="showroom-photo" role="img" aria-label="Glossy black sports hatchback parked in a dimly lit car showroom"></div>
    <div class="site-url">gearloft-example.com.au</div>
    <div class="brand">
      <p class="brand-name">Gearloft</p>
      <p class="brand-tagline">High performance vehicle importers</p>
    </div>
    <p class="headline">Industry experts<br>in imports</p>
  </div>
</body>
</html>
```